Book cover for book of Poems "Lanternfall"

I have written a book of poems. The book is titled "Lanternfall" and has 160 pages. The poems were written mostly during my youth but there are newer poems also written over the past 10 years (I'm 42 now). They are mostly about love, loss, social conformity, and nature. I'm influenced a lot by the English Romantic Poets, gothic motives, and 80s music by bands such as The Vells, Corabel & the Tarrows, and Pennock. I need an original book cover design for my book. Attached are samples of designs I like and few of my poems. The cover will be a hardcover and I need design for Front Cover, Back Cover, and Spine. Dimension is 6"x9". Front Cover should have name of book "Lanternfall" and name of author "Ravi Menhar". Thanks.
Updates

Further details which I should have included in my original brief -The book cover will be a hard cover. Design is required for front cover, back cover, and spine. Dimension is 6x9.Front should have book title "Lanternfall" and author's name "Ravi Menhar". Added Monday, December 19, 2016

Target Market(s)

Mostly friends and family

Requirements
Must have
• I don't mind a design where lanternfall is spelled out in big capital letters and text from one of my poems is inside, like the sample I've attached.

```html
<!DOCTYPE html>
<html lang="en">
<head>
<meta charset="utf-8">
<title>Lanternfall — Ravi Menhar</title>
<link href="https://fonts.googleapis.com/css2?family=Oswald:wght@600&family=Josefin+Sans:wght@300&display=swap" rel="stylesheet">
<style>
  :root {
    --backdrop: #2a2526;
    --cover-black: #0d0c0b;
    --title-gold: #dcb52c;
    --glow-core: #f4d23a;
    --glow-mid: #e79a16;
    --glow-edge: #6a3307;
    --author-white: #f2f0ea;
  }
  * { box-sizing: border-box; }
  html, body {
    margin: 0;
    width: 1200px;
    height: 960px;
    overflow: hidden;
    background: var(--backdrop);
  }
  .stage {
    width: 1200px;
    height: 960px;
    display: flex;
    align-items: center;
    justify-content: center;
  }
  .book-cover {
    position: relative;
    width: 587px;
    height: 880px;
    background: var(--cover-black);
  }
  .title-art {
    position: absolute;
    left: 0;
    top: 40px;
    width: 587px;
    height: 320px;
  }
  .title-letters {
    font-family: 'Oswald', sans-serif;
    font-weight: 600;
    fill: var(--title-gold);
  }
  .scene-photo {
    position: absolute;
    left: 0;
    top: 380px;
    width: 587px;
    height: 350px;
    background:
      linear-gradient(to bottom, var(--cover-black) 0%, transparent 12%, transparent 80%, var(--cover-black) 100%),
      linear-gradient(to right, transparent 70%, var(--cover-black) 100%),
      radial-gradient(ellipse 55% 60% at 34% 42%, var(--glow-core) 0%, var(--glow-mid) 45%, var(--glow-edge) 85%, var(--cover-black) 100%);
  }
  .author-name {
    position: absolute;
    left: 0;
    right: 0;
    top: 762px;
    margin: 0;
    text-align: center;
    font-family: 'Josefin Sans', sans-serif;
    font-weight: 300;
    font-size: 46px;
    letter-spacing: 3px;
    color: var(--author-white);
  }
</style>
</head>
<body>
<main class="stage">
  <section class="book-cover">
    <svg class="title-art" viewBox="0 0 587 320" role="img" aria-label="Lanternfall">
      <text class="title-letters" x="310" y="150" font-size="150" text-anchor="middle" textLength="390" lengthAdjust="spacingAndGlyphs">LANTERN</text>
      <text class="title-letters" x="290" y="298" font-size="150" text-anchor="middle" textLength="210" lengthAdjust="spacingAndGlyphs">FALL</text>
    </svg>
    <div class="scene-photo" role="img" aria-label="Photograph of two silhouetted figures walking through reeds beside water glowing gold and orange at sunset"></div>
    <p class="author-name">RAVI MENHAR</p>
  </section>
</main>
</body>
</html>
```